Menu Design Project for new restauranct concept

Design menu for new restaurant concept called Juniper's Burgers & Dogs. Logo is attached.

Industry/Entity Type

Restaurant

Requirements
Must have
• Menu items and pricing:

Burgers
Snack Burger $3.49
Snack Cheeseburger $3.99
Juniper's signature Burger $4.99
Juniper's signature Cheeseburger $5.49
Burger toppings: bacon, lettuce, tomato, onion, pickle, grilled onions, grilled mushrooms, grilled green peppers, jalapeƱo peppers.

Dogs
Hot Dog $2.99
Bacon Cheese Hot Dog $3.99
Slaw Dog $3.99
Kraut Dog $3.49
Chili Dog $3.99 with or with out cheese
Hot dogs are 100% beef

Other
Grilled Chicken Sandwich $5.99
Grilled Chicken Sandwich with cheese $6.49
(Same toppings as burgers)

French Fries $1.99

Loaded Potatos
The Plain Tater: $4.99 choose from: butter, sour cream, cheese, chives
The Garden Tater: $5.99 choose from: the Basic plus, broccoli & cheese, grilled mushrooms, onions, & peppers
The Rancher Tater: $6.99 choose from the Basic/Veggie plus: grilled chicken, chili, Philly cheesesteak, pulled pork.

Drinks
32oz. Drink $1.88
20oz. Drink $1.69

attached logo.
Nice to have
• love to incorporate the woodgrain backgound. It makes the logo look most like a cattle brand, which we like.

```html
<!DOCTYPE html>
<html lang="en">
<head>
<meta charset="utf-8">
<title>Juniper's Burgers &amp; Dogs — Menu</title>
<link href="https://fonts.googleapis.com/css2?family=Rubik+Dirt&family=Londrina+Solid:wght@400;900&family=Alfa+Slab+One&display=swap" rel="stylesheet">
<style>
  :root {
    --parchment-light: #efe3b0;
    --parchment-mid: #dcc77a;
    --parchment-dark: #b9a24c;
    --heading-red: #a3201c;
    --item-brown: #4a2a12;
    --note-brown: #7a6a42;
    --wood-light: #8a7a68;
    --wood-dark: #4e4236;
    --panel-dark: #241410;
    --panel-text: #e9e2d4;
  }
  * { margin: 0; padding: 0; box-sizing: border-box; }
  html, body { width: 927px; height: 1200px; overflow: hidden; background: #fff; }
  .menu { position: relative; width: 927px; height: 1200px; overflow: hidden; }

  .parchment {
    position: absolute; left: 0; top: 0; width: 586px; height: 1200px;
    background: radial-gradient(ellipse at 30% 20%, var(--parchment-light) 0%, var(--parchment-mid) 60%, var(--parchment-dark) 100%);
  }
  .woodgrain {
    position: absolute; left: 586px; top: 0; width: 341px; height: 356px;
    background: linear-gradient(180deg, var(--wood-light), var(--wood-dark));
  }
  .dark-panel {
    position: absolute; left: 586px; top: 356px; width: 341px; height: 844px;
    background: var(--panel-dark);
  }

  .section-title {
    position: absolute; left: 30px;
    font-family: "Rubik Dirt", "Londrina Solid", sans-serif;
    color: var(--heading-red); font-size: 50px; line-height: 1; letter-spacing: 1px;
  }
  .section-note {
    font-family: "Alfa Slab One", serif; color: var(--item-brown);
    font-size: 18px; letter-spacing: 0; margin-left: 14px; vertical-align: 4px;
  }

  .item {
    position: absolute; left: 58px; width: 460px;
    display: flex; justify-content: space-between; align-items: baseline;
    font-family: "Londrina Solid", sans-serif; font-weight: 900;
    color: var(--item-brown); font-size: 25px; letter-spacing: 0.5px; text-transform: uppercase; line-height: 1;
  }
  .item-aside { font-family: "Alfa Slab One", serif; font-weight: 400; font-size: 15px; text-transform: none; color: var(--note-brown); }
  .item.spud { left: 52px; width: 462px; }

  .item-detail {
    position: absolute; left: 58px; width: 470px;
    font-family: "Alfa Slab One", serif; color: var(--note-brown);
    font-size: 16.5px; line-height: 23px;
  }
  .item-detail.spud { left: 52px; }

  .brand-mark {
    position: absolute; left: 634px; top: 22px; width: 244px; height: 244px;
    border: 5px solid var(--panel-text); border-radius: 50%;
    display: flex; align-items: center; justify-content: center;
    font-family: "Londrina Solid", sans-serif; font-weight: 900; color: var(--panel-text);
    font-size: 46px;
  }
  .brand-tagline {
    position: absolute; left: 586px; width: 341px; top: 284px; text-align: center;
    font-family: "Londrina Solid", sans-serif; font-weight: 900; color: var(--panel-text);
    font-size: 40px; letter-spacing: 1px; text-transform: uppercase;
  }

  .side-block {
    position: absolute; left: 586px; width: 341px; text-align: center; color: var(--panel-text);
  }
  .side-title {
    font-family: "Londrina Solid", sans-serif; font-weight: 900; font-size: 21px;
    letter-spacing: 1px; text-transform: uppercase; margin-bottom: 28px;
  }
  .side-entry { font-family: "Alfa Slab One", serif; font-size: 17px; line-height: 23px; margin-bottom: 23px; }
</style>
</head>
<body>
<main class="menu">
  <div class="parchment" role="img" aria-label="Weathered parchment texture background"></div>
  <div class="woodgrain" role="img" aria-label="Weathered woodgrain planks background"></div>
  <div class="dark-panel"></div>

  <div class="brand-mark">Juniper's</div>
  <div class="brand-tagline">Burgers &amp; Dogs</div>

  <!-- Burgers -->
  <h2 class="section-title" style="top:44px;">Burgers</h2>
  <div class="item" style="top:122px;"><span>Snack Burger</span><span>$3.49</span></div>
  <div class="item" style="top:168px;"><span>Snack Cheeseburger</span><span>$3.99</span></div>
  <div class="item" style="top:214px;"><span>Juniper's Signature Burger</span><span>$4.99</span></div>
  <div class="item" style="top:260px;"><span>Juniper's Signature Cheeseburger</span><span>$5.49</span></div>
  <p class="item-detail" style="top:299px;">Burger Toppings: Bacon, Lettuce, Tomato, Onion, Pickle, Grilled Onions, Grilled Mushrooms, Grilled Green Peppers, Jalapeño Peppers.</p>

  <!-- Dogs -->
  <h2 class="section-title" style="top:422px;">Dogs<span class="section-note">Hot dogs are 100% beef</span></h2>
  <div class="item" style="top:506px;"><span>Hot Dog</span><span>$2.99</span></div>
  <div class="item" style="top:551px;"><span>Bacon Cheese Hot Dog</span><span>$3.99</span></div>
  <div class="item" style="top:596px;"><span>Slaw Dog</span><span>$3.99</span></div>
  <div class="item" style="top:642px;"><span>Kraut Dog</span><span>$3.49</span></div>
  <div class="item" style="top:688px;"><span>Chili Dog <span class="item-aside">with or without cheese</span></span><span>$3.99</span></div>

  <!-- Loaded Potatos -->
  <h2 class="section-title" style="top:756px; font-size:56px;">Loaded Potatos</h2>
  <div class="item spud" style="top:837px;"><span>The Plain Tater:</span><span>$4.99</span></div>
  <p class="item-detail spud" style="top:872px;">Choose From: Butter, Sour Cream,<br>Cheese, Chives</p>
  <div class="item spud" style="top:928px;"><span>The Garden Tater:</span><span>$5.99</span></div>
  <p class="item-detail spud" style="top:966px;">Choose From: The Basic Plus,<br>Broccoli &amp; Cheese, Grilled Mushrooms,<br>Onions, &amp; Peppers</p>
  <div class="item spud" style="top:1045px;"><span>The Rancher Tater:</span><span>$6.99</span></div>
  <p class="item-detail spud" style="top:1085px;">Choose From The Basic/Veggie Plus:<br>Grilled Chicken, Chili, Philly<br>Cheesesteak, Pulled Pork.</p>

  <!-- Right column -->
  <section class="side-block" style="top:424px;">
    <h3 class="side-title">Other</h3>
    <p class="side-entry">Grilled Chicken<br>Sandwich<br>$5.99</p>
    <p class="side-entry">Grilled Chicken<br>Sandwich with cheese<br>$6.49</p>
    <p class="side-entry">(Same toppings as<br>burgers)</p>
  </section>
  <section class="side-block" style="top:788px;">
    <h3 class="side-title">Sides</h3>
    <p class="side-entry">French Fries</p>
    <p class="side-entry">$1.99</p>
  </section>
  <section class="side-block" style="top:990px;">
    <h3 class="side-title">Drinks</h3>
    <p class="side-entry">32oz. Drink $1.88</p>
    <p class="side-entry">20oz. Drink $1.69</p>
  </section>
</main>
</body>
</html>
```